Airplane Billboard

This is a banner that will flown behind an airplane up 1000 ft in the air.

The size of the banner will be 25 feet high x 60 feet wide.

I'd like our logo to cover 25 feet x 25 feet- to the left side of the banner.

Then I would like the text to read : Bachelor Party Headquarters
Harlow, WI www.kvm.place

Target Market(s)

males 21-45

Font styles to use
Sans Serif

Colors

Designer to choose colors to be used in the design.

Requirements
Must have
• Our logo. I tried to attach the high resolution logo but it was too large.
• The text: Bachelor Party Headquarters
• Our location: Franklin,WI
• Our web site: www.kvm.place

```html
<!DOCTYPE html>
<html lang="en">
<head>
<meta charset="utf-8">
<title>KVM – Bachelor Party Headquarters Banner</title>
<link rel="stylesheet" href="https://fonts.googleapis.com/css2?family=Oswald:wght@500;700&family=Open+Sans:wght@700;800&display=swap">
<style>
  :root {
    --stage: #0b0b10;
    --magenta: #ff1fb8;
    --hot-pink: #f21ec4;
    --violet: #b623d6;
    --deep-violet: #6a2bd8;
    --ink: #0a0a0a;
    --white: #ffffff;
    --gold: #ffd21f;
    --gold-deep: #f2a90c;
    --crowd-warm: #ff5a3c;
    --crowd-cool: #c02ad0;
  }
  * { box-sizing: border-box; margin: 0; padding: 0; }
  html, body {
    width: 1200px; height: 949px; overflow: hidden;
    background: var(--stage);
  }
  .canvas { position: relative; width: 1200px; height: 949px; }

  .banner {
    position: absolute; left: 50px; top: 257px;
    width: 1100px; height: 435px;
    overflow: hidden;
    border: 3px solid var(--ink);
    background:
      linear-gradient(180deg, rgba(255,255,255,0) 52%, rgba(255,255,255,0.18) 58%, rgba(255,255,255,0) 64%),
      linear-gradient(180deg, var(--magenta) 0%, var(--hot-pink) 40%, var(--violet) 70%, var(--deep-violet) 100%);
  }

  .brand-mark {
    position: absolute; left: 16px; top: 6px;
    font-family: "Oswald", sans-serif; font-weight: 700;
    font-size: 236px; line-height: 1; letter-spacing: 4px;
    color: var(--ink);
  }
  .brand-name {
    position: absolute; left: 16px; top: 322px; width: 557px;
    font-family: "Oswald", sans-serif; font-weight: 700;
    font-size: 56px; line-height: 76px; letter-spacing: 1px;
    color: var(--ink); white-space: nowrap;
  }

  .headline {
    position: absolute; left: 600px; top: 30px; width: 460px;
    font-family: "Oswald", sans-serif; font-weight: 700;
    color: var(--white); text-align: center; line-height: 1.08;
    font-size: 58px; text-transform: uppercase;
  }

  .location-tag {
    position: absolute; left: 709px; top: 210px;
    width: 300px; height: 50px;
    transform: rotate(-4deg);
    background: linear-gradient(180deg, var(--gold) 0%, var(--gold-deep) 100%);
    border-radius: 4px;
    display: flex; align-items: center; justify-content: center;
    font-family: "Open Sans", sans-serif; font-weight: 800;
    font-size: 32px; color: var(--ink); white-space: nowrap;
  }

  .crowd {
    position: absolute; left: 573px; top: 268px;
    width: 527px; height: 167px;
    background: linear-gradient(90deg, var(--crowd-cool) 0%, var(--crowd-warm) 45%, var(--crowd-warm) 75%, var(--crowd-cool) 100%);
    opacity: 0.85;
    -webkit-mask-image: linear-gradient(180deg, transparent 0%, #000 35%);
            mask-image: linear-gradient(180deg, transparent 0%, #000 35%);
  }

  .web-address {
    position: absolute; left: 700px; top: 370px; width: 300px;
    text-align: center;
    font-family: "Open Sans", sans-serif; font-weight: 800;
    font-size: 30px; color: var(--white); letter-spacing: 0.5px;
    text-transform: uppercase; white-space: nowrap;
  }
</style>
</head>
<body>
  <main class="canvas">
    <section class="banner" aria-label="Airplane banner">
      <div class="brand-mark">KVM</div>
      <div class="brand-name">KINGS VELVET MILE</div>

      <h1 class="headline">Bachelor Party<br>Headquarters</h1>

      <div class="location-tag">Harlow, WI</div>

      <div class="crowd" role="img" aria-label="Silhouetted party crowd with raised hands"></div>

      <div class="web-address">www.kvm.place</div>
    </section>
  </main>
</body>
</html>
```